Travel Website Design

My client is a startup that will sell luxury hunting and fishing trips.
We do not have a logo as of yet, but I have attached 3 options for you to use in the mockup process. Please feel free to use any one (or all 3) of them, but don't base design around them.

Also attached is client's loose idea of how he wants an interior page to look. For the homepage, it would definitely need a rotating image slider, a search, and a tabbed section. The crestpinesafaris.com is probably closest to what he is looking for.

Here are a few websites to pass along. In addition to the logos I have attached some links of company websites that are competition and have similar designs and layouts similar to what I am looking for.

http://www.crestpinesafaris.com - The most direct competition that I have. I really like how they layout the pages and lodges info.

Varno.com - Close competition. Not a huge fan of how they search for lodges but like how they display each lodge and provide info.

http://www.qrandel.com/ - Example of a company website and layout the client does not like.

http://stonemeadjourneys.com/ - Clean feel. Not a fan of how they layout each lodges info.

```html
<!DOCTYPE html>
<html lang="en">
<head>
<meta charset="utf-8">
<title>Website Name – Luxury Hunting &amp; Fishing Trips</title>
<link rel="stylesheet" href="https://fonts.googleapis.com/css2?family=Open+Sans:wght@400;600;700&family=Ubuntu:wght@400;500&family=Titan+One&family=Cabin+Sketch:wght@700&family=Oswald:wght@400&display=swap">
<style>
:root{
  --red:#a81f24;
  --red-dark:#7d1418;
  --orange:#e5a029;
  --orange-dark:#c9861a;
  --ink:#333;
  --muted:#555;
  --nav-bg:rgba(236,236,232,.92);
  --panel:rgba(236,238,236,.9);
  --footer-links:#3c3c3c;
  --footer:#2a2a2a;
  --white:#fff;
}
*{box-sizing:border-box;margin:0;padding:0}
html,body{width:1085px;height:1200px;overflow:hidden}
body{position:relative;font-family:"Ubuntu",sans-serif;color:var(--ink);background:#3a4a3c}
.abs{position:absolute}
.backdrop{left:0;top:0;width:1085px;height:1095px;
  background:radial-gradient(ellipse at 95% 60%,#c4561a 0,#8a3a14 12%,transparent 30%),
  radial-gradient(ellipse at 90% 5%,#d9c25a 0,transparent 35%),
  linear-gradient(90deg,#1f3a33 0%,#4c5a3a 20%,#9a8a4a 60%,#c7a744 85%,#b5732a 100%)}
.backdrop::after{content:"";position:absolute;left:0;right:0;bottom:0;height:330px;
  background:linear-gradient(180deg,transparent,#4a3a1c 60%,#2a2418)}
.topbar{left:0;top:0;width:1085px;height:39px}
.contact-top{right:192px;top:10px;display:flex;gap:16px;align-items:center;
  font-family:"Oswald",sans-serif;font-size:13px;color:var(--white)}
.contact-top span{display:flex;align-items:center;gap:5px}
.social{display:flex;gap:3px}
.social i{display:block;width:12px;height:12px;border-radius:50%;background:var(--white)}
.navband{left:0;top:39px;width:1085px;height:53px;background:var(--nav-bg)}
.brand{left:191px;top:0;width:111px;height:116px;background:var(--white);
  display:flex;flex-direction:column;align-items:center;justify-content:flex-end;padding-bottom:10px;z-index:3}
.brand-dot{width:46px;height:46px;border-radius:50%;background:var(--orange);margin-bottom:14px}
.brand-name{font-family:"Open Sans",sans-serif;font-weight:600;font-size:12px;color:var(--ink)}
.mainnav{left:353px;top:36px;display:flex;align-items:center;height:59px;z-index:3}
.mainnav a{font-family:"Open Sans",sans-serif;font-weight:700;font-size:10px;color:#3a3a3a;
  text-decoration:none;padding:0 12px;line-height:59px}
.mainnav a.active{background:var(--orange);color:var(--white);width:54px;padding:0;text-align:center}
.slider{left:191px;top:92px;width:702px;height:285px;border:3px solid var(--white);
  background:linear-gradient(180deg,#5f8fbf 0%,#8ab3d8 30%,#3d6f9c 55%,#22507a 100%)}
.slider-copy{left:26px;top:168px;color:var(--white)}
.slider-kicker{font-family:"Ubuntu",sans-serif;font-size:14px;letter-spacing:.3px}
.slider-title{font-family:"Cabin Sketch",sans-serif;font-weight:700;font-size:32px;line-height:35px;margin-top:2px}
.dots{left:504px;top:359px;width:78px;height:23px;background:var(--red);
  display:flex;gap:4px;justify-content:center;align-items:center}
.dots i{width:9px;height:9px;border-radius:50%;background:var(--white)}
.dots i.on{background:var(--red);border:2px solid var(--white)}
.locator{left:191px;top:393px;width:702px;height:51px}
.locator-title{left:81px;top:15px;font-family:"Titan One",sans-serif;font-size:17px;color:var(--white)}
.select{left:314px;top:9px;width:200px;height:34px;background:var(--white);border:2px solid #ddd;
  font-family:"Open Sans",sans-serif;font-size:10px;color:#666;padding:9px 11px;font-weight:600}
.select-caret{right:7px;top:6px;width:19px;height:19px;background:var(--orange)}
.book{left:526px;top:9px;width:96px;height:33px;background:var(--orange);
  font-family:"Titan One",sans-serif;color:var(--white);font-size:13px;text-align:center;line-height:33px}
.content{left:191px;top:459px;width:702px;height:636px;background:var(--panel)}
.welcome{left:0;top:17px;width:702px;text-align:center;font-family:"Titan One",sans-serif;font-size:16px;color:var(--red)}
.intro{left:25px;top:44px;width:652px;font-size:9.6px;line-height:15.2px;color:#444}
.tabs{left:22px;top:149px;display:flex;gap:5px}
.tabs span{height:29px;line-height:30px;padding:0 15px;font-family:"Titan One",sans-serif;font-size:12.5px;
  color:var(--white);background:var(--orange)}
.tabs span.active{background:var(--red)}
.tab-panel{left:22px;top:178px;width:660px;height:218px;
  background:linear-gradient(180deg,#e8eef2 0%,#d6e2ea 45%,#c4d6e2 100%)}
.group{position:absolute}
.group h3{font-family:"Ubuntu",sans-serif;font-weight:500;font-size:14px;color:var(--orange);margin-bottom:6px}
.group svg{display:block;margin-bottom:8px}
.group ul{list-style:none;columns:var(--cols,1);column-gap:22px;font-family:"Open Sans",sans-serif;font-weight:600;font-size:9.5px;color:#555}
.group li{line-height:15.5px;padding-left:14px;position:relative}
.group li::before{content:"";position:absolute;left:0;top:4px;width:5px;height:5px;border:2px solid var(--orange);border-radius:50%}
.similar{left:22px;top:424px;width:660px;height:187px;background:var(--white)}
.similar-title{left:278px;top:-6px;width:142px;height:29px;background:var(--red);color:var(--white);
  font-family:"Titan One",sans-serif;font-size:14px;text-align:center;line-height:29px}
.thumb{top:40px;width:140px;height:126px}
.arrow{top:85px;width:22px;height:36px;background:var(--white);display:flex;align-items:center;justify-content:center}
.footer-links{left:0;top:1095px;width:1085px;height:38px;background:var(--footer-links);
  display:flex;justify-content:center;gap:18px;align-items:center}
.footer-links a{font-size:10px;color:var(--white);text-decoration:none}
.footer{left:0;top:1133px;width:1085px;height:67px;background:var(--footer)}
.subscribe-label{left:193px;top:10px;font-size:9.5px;color:var(--orange)}
.email-field{left:193px;top:27px;width:143px;height:28px;background:var(--white);font-size:8.5px;color:#444;padding:9px 11px}
.submit{left:344px;top:27px;width:68px;height:28px;background:var(--orange);color:var(--white);
  font-family:"Open Sans",sans-serif;font-weight:700;font-size:10px;text-align:center;line-height:28px}
.footer-contact{right:192px;top:19px;display:flex;gap:12px;align-items:center;font-size:8.5px;color:#bbb}
.footer-contact span{display:flex;align-items:center;gap:5px}
.footer-contact .social i{background:var(--orange)}
.copyright{right:192px;top:41px;font-size:8px;color:#bbb}
</style>
</head>
<body>
<div class="abs backdrop" role="img" aria-label="Blurred sunset lake scene with an angler in silhouette"></div>

<header>
  <div class="abs topbar">
    <div class="abs contact-top">
      <span><svg width="13" height="10" viewBox="0 0 13 10"><rect width="13" height="10" fill="#fff"/><path d="M0 0l6.5 5L13 0" stroke="#555" fill="none"/></svg>INFO@TRAILHAVEN.COM</span>
      <span><svg width="11" height="11" viewBox="0 0 24 24"><path fill="#fff" d="M6.6 10.8a15 15 0 006.6 6.6l2.2-2.2c.3-.3.7-.4 1-.2 1.1.4 2.3.6 3.6.6.6 0 1 .4 1 1V20c0 .6-.4 1-1 1A17 17 0 013 4c0-.6.4-1 1-1h3.5c.6 0 1 .4 1 1 0 1.3.2 2.5.6 3.6.1.3 0 .7-.2 1z"/></svg>555-204-7193</span>
      <span class="social"><i></i><i></i><i></i><i></i></span>
    </div>
  </div>
  <div class="abs navband"></div>
  <div class="abs brand">
    <div class="brand-dot"></div>
    <div class="brand-name">WEBSITE NAME</div>
  </div>
  <nav class="abs mainnav">
    <a class="active" href="#">HOME</a>
    <a href="#">CONSERVATION</a>
    <a href="#">BLOG</a>
    <a href="#">TRAVEL TOOLS</a>
    <a href="#">BECOME A MEMBER</a>
    <a href="#">CONTACT US</a>
  </nav>
</header>

<section class="abs slider" role="img" aria-label="Angler on open sea holding up a large barracuda">
  <div class="abs slider-copy">
    <div class="slider-kicker">Expert Guidance &amp; Zero Extra Cost</div>
    <div class="slider-title">DON'T LET THIS<br>ONE GET AWAY...</div>
  </div>
</section>
<div class="abs dots"><i></i><i></i><i class="on"></i><i></i><i></i></div>

<section class="abs locator">
  <svg class="abs" style="left:0;top:0" width="702" height="51" viewBox="0 0 702 51"><path d="M0 0H702L682 25.5 702 51H0L20 25.5Z" fill="#a81f24"/></svg>
  <div class="abs locator-title">SELECT YOUR LOCATION</div>
  <div class="abs select">CHOSE DESTINATION
    <div class="abs select-caret"><svg width="19" height="19" viewBox="0 0 19 19"><path d="M6.5 8h6l-3 4z" fill="#fff"/></svg></div>
  </div>
  <div class="abs book">BOOK NOW</div>
</section>

<main class="abs content">
  <h1 class="abs welcome">WELCOME TO COMPANY NAME</h1>
  <p class="abs intro">Lorem ipsum dolor sit amet, consectetur adipiscing elit. Vivamus diam arcu, commodo eget rutrum id, faucibus ac ex. Fusce at laoreet ligula. Sed interdum blandit luctus. Maecenas imperdiet arcu quis tincidunt commodo. Sed tempor felis nunc, eget gravida risus tincidunt in. In pharetra vitae nunc eu fermentum. Phasellus semper, enim quis dapibus condimentum, mauris nisi volutpat nisi, at egestas ligula mi vel eros. Donec non lacus ipsum. Pellentesque blandit ullamcorper lectus vitae vulputate. Suspendisse mollis, justo eu dapibus vestibulum, eros lorem sodales risus, in vehicula quam tellus ac odio. Morbi rhoncus, tortor ut condimentum iaculis, libero magna faucibus felis, quis condimentum nibh augue nec risus. Morbi gravida feugiat pellentesque.</p>

  <div class="abs tabs">
    <span class="active">Trip/Accomodation</span><span>Packages</span><span>Conditions</span><span>Fast Facts</span>
  </div>
  <div class="abs tab-panel" role="img" aria-label="Faded view of fishing rods on a boat wake at sea">
    <div class="group" style="left:25px;top:24px">
      <h3>Category</h3>
      <svg width="170" height="8" viewBox="0 0 170 8"><path d="M0 6Q85 2 168 5" stroke="#e5a029" fill="none" stroke-width="1.3"/></svg>
      <ul><li>Ski</li><li>Heli</li></ul>
    </div>
    <div class="group" style="left:250px;top:24px">
      <h3>Accomodation</h3>
      <svg width="170" height="8" viewBox="0 0 170 8"><path d="M0 6Q85 2 168 5" stroke="#e5a029" fill="none" stroke-width="1.3"/></svg>
      <ul><li>Lodge</li><li>Hotel</li></ul>
    </div>
    <div class="group" style="left:463px;top:24px;--cols:2">
      <h3>Suited for</h3>
      <svg width="170" height="8" viewBox="0 0 170 8"><path d="M0 6Q85 2 168 5" stroke="#e5a029" fill="none" stroke-width="1.3"/></svg>
      <ul><li>Family</li><li>Couples</li><li>Solo Travellers</li><li>Groups</li></ul>
    </div>
    <div class="group" style="left:25px;top:127px;--cols:2">
      <h3>Activities</h3>
      <svg width="170" height="8" viewBox="0 0 170 8"><path d="M0 6Q85 2 168 5" stroke="#e5a029" fill="none" stroke-width="1.3"/></svg>
      <ul><li>Wifi</li><li>Spa</li><li>Pool Table</li></ul>
    </div>
  </div>

  <section class="abs similar">
    <div class="abs arrow" style="left:-8px"><svg width="10" height="12" viewBox="0 0 10 12"><path d="M8 1L3 6l5 5" stroke="#a81f24" stroke-width="3" fill="none"/></svg></div>
    <div class="abs thumb" style="left:23px;background:linear-gradient(160deg,#c9b48a,#8a6a44)" role="img" aria-label="Family fishing trip by a tent"></div>
    <div class="abs thumb" style="left:182px;background:linear-gradient(160deg,#5a5048,#2e2a26)" role="img" aria-label="Angler casting at dusk"></div>
    <div class="abs thumb" style="left:340px;background:linear-gradient(180deg,#9cc1dc,#3d5d78 60%,#1f3040)" role="img" aria-label="Fishing boat on calm water"></div>
    <div class="abs thumb" style="left:497px;background:linear-gradient(180deg,#6fa3d2,#2b5a88 55%,#c9a347)" role="img" aria-label="Trolling rods on a boat at sea"></div>
    <div class="abs arrow" style="right:-8px"><svg width="10" height="12" viewBox="0 0 10 12"><path d="M2 1l5 5-5 5" stroke="#a81f24" stroke-width="3" fill="none"/></svg></div>
    <h2 class="abs similar-title">Similar Trips</h2>
  </section>
</main>

<nav class="abs footer-links">
  <a href="#">Trip Details</a><a href="#">Accomodations</a><a href="#">Rates</a><a href="#">Other Info</a><a href="#">Faq's</a><a href="#">Terms</a><a href="#">Contact Us</a><a href="#">Reviews</a>
</nav>
<footer class="abs footer">
  <div class="abs subscribe-label">Subscribe to exclusive Trips</div>
  <div class="abs email-field">Email Address</div>
  <div class="abs submit">SUBMIT</div>
  <div class="abs footer-contact">
    <span><svg width="11" height="8" viewBox="0 0 13 10"><rect width="13" height="10" fill="#e5a029"/><path d="M0 0l6.5 5L13 0" stroke="#2a2a2a" fill="none"/></svg>info@trailhaven.com</span>
    <span><svg width="9" height="9" viewBox="0 0 24 24"><path fill="#e5a029" d="M6.6 10.8a15 15 0 006.6 6.6l2.2-2.2c.3-.3.7-.4 1-.2 1.1.4 2.3.6 3.6.6.6 0 1 .4 1 1V20c0 .6-.4 1-1 1A17 17 0 013 4c0-.6.4-1 1-1h3.5c.6 0 1 .4 1 1 0 1.3.2 2.5.6 3.6.1.3 0 .7-.2 1z"/></svg>555-204-7193</span>
    <span class="social"><i></i><i></i><i></i><i></i></span>
  </div>
  <div class="abs copyright">© Company Name 2014. All rights reserved.</div>
</footer>
</body>
</html>
```